New brand for digital company - your chance to get creative

We need to create a brand for our new business 'Lanternfield Digital'. Please read the brief below before progressing as we are looking for some quite specific outputs.

Background

We are positioning ourselves as ‘marketing technologists’ - we're helping businesses engage with their customers in the online space.

Our tactics include branding, marketing, online management, and social media, however we are differentiating ourselves by focusing on overall strategy, not just tactics. Our tagline is ‘Online made simple’.

We have stipulated some parameters for the brand but otherwise want designers to exercise their creativity.

Requirements
Must have
• We want to see an entire concept, not just a logo.

```html
<!DOCTYPE html>
<html lang="en">
<head>
<meta charset="utf-8">
<title>Lanternfield Digital – Brochure Spread</title>
<link href="https://fonts.googleapis.com/css2?family=Titillium+Web:wght@400;600;700&display=swap" rel="stylesheet">
<style>
  :root {
    --brand-red: #df0a3a;
    --brand-orange: #f28c00;
    --paper: #f7f7f7;
    --canvas: #ffffff;
    --ink: #222222;
    --photo-city: #8a8578;
    --photo-forest: #5d6650;
    --photo-skin: #c9a58c;
  }
  * { margin: 0; padding: 0; box-sizing: border-box; }
  html, body { width: 1200px; height: 1000px; overflow: hidden; background: var(--canvas); }
  body { font-family: "Titillium Web", Arial, sans-serif; color: var(--ink); position: relative; }

  .spread { position: absolute; left: 107px; top: 230px; width: 984px; height: 538px; }
  .page { position: absolute; top: 0; height: 538px; }
  .page--cover { left: 0; width: 326px; background: var(--paper); }
  .page--feature { left: 326px; width: 330px; background: var(--brand-red); }
  .page--article { left: 656px; width: 328px; background: var(--paper); }

  .block { position: absolute; }
  .block--orange { background: var(--brand-orange); }

  .photo { position: absolute; }
  .photo--eye { background: linear-gradient(180deg, #d8b9a0, var(--photo-skin) 60%, #a88670); }
  .photo--street { background: linear-gradient(180deg, #b8bcc0 0%, var(--photo-city) 45%, #4f4d48 100%); }
  .photo--forest { background: linear-gradient(180deg, #3e4a36 0%, var(--photo-forest) 55%, #a8a89a 100%); }

  .cover-name {
    position: absolute; left: 128px; top: 246px;
    display: flex; align-items: center; gap: 6px;
    font-weight: 700; font-size: 15px; color: var(--brand-red); line-height: 1;
  }
  .cover-name__square { width: 10px; height: 10px; background: var(--brand-orange); }

  .feature-name {
    position: absolute; left: 190px; top: 222px;
    font-weight: 400; font-size: 13px; color: #fff; line-height: 1;
  }

  .article-title {
    position: absolute; left: 18px; top: 30px; width: 300px;
    font-weight: 700; font-size: 28px; line-height: 30px; color: var(--brand-red);
  }
  .article-rule { position: absolute; right: 0; top: 110px; width: 8px; height: 133px; background: var(--brand-red); }

  .article-body { position: absolute; left: 125px; top: 240px; width: 176px; }
  .article-body h2 { font-weight: 700; font-size: 13px; line-height: 16px; color: var(--brand-red); }
  .article-body .intro { font-weight: 600; font-size: 5px; line-height: 5.6px; margin-top: 1px; }
  .article-body p { font-size: 6.6px; line-height: 7.6px; margin-top: 7px; }

  .chart { position: absolute; left: 18px; top: 276px; }
  .chart-caption { position: absolute; left: 18px; top: 346px; width: 88px; font-size: 4.6px; line-height: 5.2px; font-weight: 600; }

  .footer-name { position: absolute; left: 18px; top: 525px; font-size: 5px; font-weight: 700; }
  .footer-mark { position: absolute; right: 8px; bottom: 6px; width: 12px; height: 12px; background: var(--brand-red); }
</style>
</head>
<body>
  <div class="spread">
    <section class="page page--cover">
      <div class="cover-name"><span class="cover-name__square"></span>Lanternfield Digital</div>
    </section>

    <section class="page page--feature">
      <div class="block block--orange" style="left:73px;top:37px;width:54px;height:54px"></div>
      <div class="photo photo--eye" role="img" aria-label="Close-up photograph in skin tones framed by a grid of dots" style="left:127px;top:91px;width:56px;height:57px"></div>
      <div class="photo photo--street" role="img" aria-label="Photograph of a steep city street lined with houses" style="left:56px;top:225px;width:128px;height:127px"></div>
      <div class="feature-name">Lanternfield Digital</div>
      <div class="block block--orange" style="left:263px;top:301px;width:51px;height:51px"></div>
      <div class="block block--orange" style="left:17px;top:352px;width:39px;height:39px"></div>
      <div class="photo photo--forest" role="img" aria-label="Photograph of a path through a narrow green gorge" style="left:184px;top:352px;width:79px;height:79px"></div>
    </section>

    <section class="page page--article">
      <h1 class="article-title">Lorem ipsum dolor sit amet, consectetur adipiscing elit.</h1>
      <div class="article-rule"></div>

      <svg class="chart" width="92" height="66" viewBox="0 0 92 66" aria-label="Bar chart by year">
        <g fill="#3a3a3a">
          <rect x="0" y="2" width="8" height="48" rx="4"/><rect x="11" y="2" width="8" height="48" rx="4"/>
          <rect x="22" y="2" width="8" height="48" rx="4"/><rect x="33" y="2" width="8" height="48" rx="4"/>
          <rect x="44" y="2" width="8" height="48" rx="4"/><rect x="55" y="2" width="8" height="48" rx="4"/>
          <rect x="66" y="2" width="8" height="48" rx="4"/><rect x="77" y="2" width="8" height="48" rx="4"/>
        </g>
        <rect x="0" y="40" width="8" height="10" rx="4" fill="#df0a3a"/>
        <rect x="11" y="36" width="8" height="14" rx="4" fill="#f28c00"/>
        <rect x="22" y="31" width="8" height="19" rx="4" fill="#c9b400"/>
        <rect x="33" y="27" width="8" height="23" rx="4" fill="#8fb33a"/>
        <rect x="44" y="23" width="8" height="27" rx="4" fill="#9aa86a"/>
        <rect x="55" y="18" width="8" height="32" rx="4" fill="#8fa3a8"/>
        <rect x="66" y="10" width="8" height="40" rx="4" fill="#3fa7b8"/>
        <rect x="77" y="2" width="8" height="48" rx="4" fill="#6ec0e6"/>
        <g font-size="3" fill="#999" font-family="Titillium Web, sans-serif">
          <circle cx="4" cy="56" r="1" fill="#df0a3a"/><circle cx="15" cy="56" r="1" fill="#f28c00"/>
          <circle cx="26" cy="56" r="1" fill="#c9b400"/><circle cx="37" cy="56" r="1" fill="#8fb33a"/>
          <circle cx="48" cy="56" r="1" fill="#9aa86a"/><circle cx="59" cy="56" r="1" fill="#8fa3a8"/>
          <circle cx="70" cy="56" r="1" fill="#3fa7b8"/><circle cx="81" cy="56" r="1" fill="#6ec0e6"/>
          <text x="1" y="62">2005</text><text x="12" y="62">2006</text><text x="23" y="62">2007</text><text x="34" y="62">2008</text>
          <text x="45" y="62">2009</text><text x="56" y="62">2010</text><text x="67" y="62">2011</text><text x="78" y="62">2012</text>
        </g>
      </svg>
      <p class="chart-caption">Lorem ipsum dolor sit amet, consectetur adipiscing elit. Integer quis risus.</p>

      <article class="article-body">
        <h2>Lorem ipsum dolor sit amet</h2>
        <p class="intro">Lorem ipsum dolor sit amet, consectetur adipiscing elit. Integer quis risus eu sapien aliquet ullamcorper. Cras ante tortor, aliquam eu lacinia a, tempus non erat.</p>
        <p>Lorem ipsum dolor sit amet, consectetur adipiscing elit. Integer quis risus eu sapien aliquet ullamcorper. Cras ante tortor, aliquam eu lacinia a, tempus non erat. Ut ut fermentum mauris. Nullam consectetur, diam quis volutpat viverra, ligula purus laoreet nisl, at sagittis mi nisi vel odio. Quisque cursus, tortor nec luctus fermentum, metus neque pretium erat, eget ultricies metus nibh vitae augue. Nullam felis odio, feugiat a condimentum sit amet, iaculis id lacus. Vivamus sollicitudin, elit quis viverra lobortis, dolor leo cursus orci, id mollis diam orci eu eros. Praesent egestas, velit sit amet ultricies congue, nulla lectus pellentesque leo, id mattis enim magna vel quam. Fusce sit amet mauris lacus. Etiam sed risus felis, a ultrices lorem. Etiam tincidunt adipiscing rhoncus. Vestibulum hendrerit imperdiet quam vel adipiscing.<br>–</p>
        <p>Phasellus sed purus sit amet urna posuere ornare. Cras sed augue ut ante cursus vulputate sit amet sed magna. Donec et faucibus nisl. Duis tellus neque, sagittis at lobortis vel, fringilla mollis risus.<br>–</p>
        <p>Proin consequat libero eu lacus ultrices congue. Maecenas commodo elit in dolor commodo id commodo ligula euismod. Morbi mattis blandit molestie. Pellentesque nec dui id nulla ornare tincidunt. Maecenas euismod congue turpis, sit amet lacinia tellus porttitor vel. Integer ac sodales lectus. Sed in tortor id neque ornare dignissim. Nullam et nibh lacus. Curabitur mattis quam ac ante posuere dignissim. In sollicitudin congue iaculis. Nunc in ligula vel massa tincidunt tempor.</p>
      </article>

      <div class="footer-name">Lanternfield Digital</div>
      <div class="footer-mark"></div>
    </section>
  </div>
</body>
</html>
```